Social Business Consultancy

Makoro Ventures is a start up consultancy but with a difference: were non-corporate. We work in the field of economic development in low income countries and we focus on entrepreneurship but with a social and or environmental mission.

The type of projects we work on are innovative, ground breaking, different, edgy and bold. We are young, determined, , unreasonnable and undeterred by challenges.
We want our website to convey these ideas.
Updates

Hello,

Could you please include the option of having the website in two languages. Thank you.

Please note that new files have been added to the project brief.

- FrontPage  Main Photo (Grey dirt Road)
- WordCloud Photo to be used on the home page (as a small image )

The website should keep these colour tones.

Thank you !

Hello,

Wireframes have been uploaded. Please use as an indication.

Thanks,
n.

Target Market(s)

Governments, development agencies, social investors, NGOs, banks and social entrepreneurs.

Industry/Entity Type

Consulting

Requirements
Must have
• We already have a logo and business cards (provided). We want the website to look professional, yet simple with a maximum of two or three colours. We want the look to be seamless. There is no need for too many boxes or categories.
Nice to have
• We want bold, edgy, modern  and professional look .
• Examples:
• http://www.brightlanecollective.org/
• http://www.pagemorph.com/
• http://www.tallyhiring.co.nz/
Should not have
• The design should not use old style fonts.

```html
<!DOCTYPE html>
<html lang="en">
<head>
<meta charset="utf-8">
<title>Makoro Ventures — Social Business Initiatives</title>
<link rel="stylesheet" href="https://fonts.googleapis.com/css2?family=Questrial&family=Pathway+Gothic+One&family=Josefin+Slab:wght@400;600&family=Noto+Sans:wght@400;700&family=Ubuntu:wght@500;700&display=swap">
<style>
  :root {
    --sky: #14b4f0;
    --sky-deep: #0a8fd8;
    --ink: #1a1a1a;
    --text: #333333;
    --grey-band: #636363;
    --lime: #cfe22a;
    --white: #ffffff;
    --rule: #c9c9c9;
    --panel-top: #0d4f78;
    --panel-bottom: #10a7e8;
  }
  html, body { margin: 0; padding: 0; }
  body {
    width: 1200px; height: 968px; overflow: hidden; position: relative;
    background: var(--white); color: var(--text);
    font-family: "Noto Sans", Verdana, sans-serif;
  }
  .main-nav {
    position: absolute; left: 0; top: 0; width: 1200px; height: 89px;
    background: linear-gradient(#27c3fb, var(--sky-deep) 50%, var(--sky));
    display: flex; align-items: center; justify-content: center;
    font-family: "Questrial", sans-serif; font-size: 23px; color: var(--white);
  }
  .main-nav a { color: var(--white); text-decoration: none; }
  .main-nav .sep { margin: 0 28px; }
  .hero {
    position: absolute; left: 8px; top: 97px; width: 910px; height: 405px;
    background: #000;
  }
  .hero-visual {
    position: absolute; left: 0; top: 0; width: 380px; height: 405px;
    background: radial-gradient(ellipse at 45% 35%, #3a2a5a 0%, #0f3a66 35%, #061726 65%, #000 100%);
  }
  .hero-lines {
    position: absolute; left: 392px; top: 132px; margin: 0;
    font-family: "Questrial", sans-serif; font-weight: 400;
    font-size: 39px; line-height: 51px; color: var(--white);
  }
  .hero-tag {
    position: absolute; right: 38px; top: 304px;
    font-family: "Questrial", sans-serif; font-size: 20px; color: var(--lime);
  }
  .brand {
    position: absolute; left: 925px; top: 150px; width: 269px;
    text-align: center;
  }
  .brand-name {
    font-family: "Questrial", sans-serif; font-size: 30px; color: var(--ink); line-height: 1;
  }
  .brand-sub { font-family: "Noto Sans", sans-serif; font-size: 14px; color: var(--ink); margin-top: 14px; }
  .contact-panel {
    position: absolute; left: 923px; top: 263px; width: 269px; height: 239px;
    background: linear-gradient(var(--panel-top), var(--panel-bottom));
    color: var(--white); box-sizing: border-box; padding: 12px 10px;
  }
  .contact-panel h3 {
    margin: 0; font-family: "Pathway Gothic One", sans-serif; font-weight: 400; font-size: 31px; line-height: 34px;
  }
  .contact-phone { font-family: "Questrial", sans-serif; font-size: 26px; margin: 4px 0 8px 6px; white-space: nowrap; }
  .contact-label { font-family: "Ubuntu", sans-serif; font-weight: 700; font-size: 20px; color: var(--lime); margin-top: 8px; line-height: 22px; }
  .contact-value { font-size: 12px; font-weight: 700; color: #000; white-space: nowrap; }
  .team-photo-frame {
    position: absolute; left: 10px; top: 512px; width: 372px; height: 180px;
    background: #d8d8d8; box-shadow: 0 3px 3px rgba(0,0,0,.25);
  }
  .team-photo {
    position: absolute; left: 8px; top: 8px; width: 356px; height: 164px;
    background: linear-gradient(100deg, #b9c2c6, #e9e4df 45%, #9aa9b1);
  }
  .section-title {
    margin: 0; font-family: "Josefin Slab", serif; font-weight: 600; font-size: 20px; color: var(--sky);
  }
  .section-title span { color: var(--ink); font-family: "Questrial", sans-serif; font-weight: 400; font-size: 23px; }
  .welcome { position: absolute; left: 403px; top: 508px; width: 790px; }
  .welcome p { margin: 6px 0 18px; font-size: 13.5px; line-height: 21px; text-align: justify; }
  .column { position: absolute; top: 713px; }
  .column .section-title { padding-bottom: 4px; border-bottom: 1px solid var(--rule); }
  .column p { margin: 6px 0 0; font-size: 13.5px; line-height: 19.5px; }
  .col-info { left: 10px; width: 548px; }
  .col-info p { width: 540px; font-size: 14.2px; }
  .col-events { left: 606px; width: 588px; }
  .col-divider { position: absolute; left: 586px; top: 750px; width: 1px; height: 60px; background: var(--rule); }
  .site-footer {
    position: absolute; left: 0; top: 856px; width: 1200px; height: 112px; background: var(--grey-band);
  }
  .footer-nav {
    position: absolute; left: 0; top: 36px; width: 925px; text-align: center;
    font-family: "Questrial", sans-serif; font-size: 13px; color: var(--white);
  }
  .footer-nav .sep { margin: 0 8px; }
  .copyright { position: absolute; left: 0; top: 60px; width: 925px; text-align: center; font-family: "Questrial", sans-serif; font-size: 13px; color: var(--white); }
  .address {
    position: absolute; left: 923px; top: 0; width: 269px; height: 112px; background: var(--sky);
    box-sizing: border-box; padding: 26px 12px; font-family: "Ubuntu", sans-serif; font-weight: 700;
    font-style: normal; font-size: 14px; line-height: 17px; color: #000;
  }
</style>
</head>
<body>
  <nav class="main-nav">
    <a href="#">Home</a><span class="sep">|</span>
    <a href="#">About Us</a><span class="sep">|</span>
    <a href="#">Our Mission</a><span class="sep">|</span>
    <a href="#">Services</a><span class="sep">|</span>
    <a href="#">Solutions</a><span class="sep">|</span>
    <a href="#">Clients</a><span class="sep">|</span>
    <a href="#">Blogs</a><span class="sep">|</span>
    <a href="#">Contact Us</a>
  </nav>

  <section class="hero">
    <div class="hero-visual" role="img" aria-label="Glowing profile of a human head with a colourful brain"></div>
    <h1 class="hero-lines">Innovative Thinking<br>Reducing Poverty<br>Changing Lives</h1>
    <div class="hero-tag">makoro,Social Business Initiatives</div>
  </section>

  <div class="brand">
    <div class="brand-name">Makoro Ventures</div>
    <div class="brand-sub">Social Business Initiatives</div>
  </div>

  <aside class="contact-panel">
    <h3>Call Us</h3>
    <div class="contact-phone">+33(0)6 41 27 53 60</div>
    <h3>Mail Us</h3>
    <div class="contact-label">Email :</div>
    <div class="contact-value">mira.delacroix@makoroventures.com</div>
    <div class="contact-label">Skype :</div>
    <div class="contact-value">mira.delacroix</div>
  </aside>

  <div class="team-photo-frame">
    <div class="team-photo" role="img" aria-label="Three young business people standing together"></div>
  </div>

  <section class="welcome">
    <h2 class="section-title">welcome to <span>MAKORO</span></h2>
    <p>Lorem ipsum dolor sit amet, consetetur sadipscing elitr, sed diam nonumy eirmod tempor invidunt ut labore et dolore magna aliquyam erat, sed diam voluptua. At vero eos et accusam et justo duo dolores et ea rebum. Stet clita kasd gubergren, no sea takimata sanctus est Lorem ipsum dolor sit amet.</p>
    <p>Lorem ipsum dolor sit amet, consetetur sadipscing elitr, sed diam nonumy eirmod tempor invidunt ut labore et dolore magna aliquyam erat, sed diam voluptua. At vero eos et accusam et justo duo dolores et ea rebum. Stet clita kasd</p>
  </section>

  <section class="column col-info">
    <h2 class="section-title">presentation <span>INFORMATION</span></h2>
    <p>Vivamus mattis odio ut arcu malesuada vehicula. Pellentesque nec massa quis turpis ornare aliquet a venenatis neque. Aenean fermentum eros sit amet nulla sagittis quis venenatis ipsum convallis. Cras leo risus, elementum nec elementum id.</p>
  </section>
  <div class="col-divider"></div>
  <section class="column col-events">
    <h2 class="section-title">events <span>FEED</span></h2>
    <p>Ut ut urna libero, eget malesuada ante. Aliquam eu lectus id dolor hendrerit accumsan id nec nulla. Suspendisse potenti. Etiam in nisi nibh, ut pulvinar mi. Aliquam sodales congue urna, in dapibus ligula laoreet non. Suspendisse gravida, lorem id mollis tristique,</p>
  </section>

  <footer class="site-footer">
    <div class="footer-nav">Home<span class="sep">|</span>About Us<span class="sep">|</span>Our Mission<span class="sep">|</span>Services<span class="sep">|</span>Solutions<span class="sep">|</span>Clients<span class="sep">|</span>Blogs<span class="sep">|</span>Contact Us</div>
    <div class="copyright">© 2010 Makoroventures.com | All rights reserved</div>
    <address class="address">"le héron"<br>32 Boulevard des Oliviers<br>98000 MONACO</address>
  </footer>
</body>
</html>
```